Two Wine Labels, One Red One White

We are looking to create a brand image for our wines. There are two requirements by law that we need, however beyond that, the creativity comes from the designer. Required are:
On The Red Label, Alcohol 14.1White Label Alcohol 12.5, The Size, 750ML
SO One label for the red wine with alcohol at 14.1 in a 750 ML Bottle, and one Label for white with alcohol at 12.5 in a 750 ML bottle.

Hi All:
I have some more clarity to assist in the design work.
The Brand Name of the wine is Valmaren for both the red and the white
The name should appear as Valmaren with the Brackets around phonetical as seen here
[vahl-mah-ren] Both the word and the phonetical spelling should appear.
and can be seen on wordplenk.com The Brand Name text can be black
Label should be very light grey, I am trying to capture a Stone grey or texture from stone, although, NOT Marble.
The Red Label, The word "Red" should be in red
The White Label, The word "White" should be in White, all the original remaining elements remain as originally posted.

I look forward to hearing from you for any additional questions.
Updates

Just added a logo Not really seeing what we are trying to achieve, maybe using the logo in the design may assist

Target Market(s)

Wine Aficionados

Requirements
Must have
• Details described in Project Description above, these are required by law. The Name of the Brand will be posted shortly. For the moment if you take the project, just place red on one label and white on the other.
Nice to have
• These two wines are from California (USA), so the Sierra Nevada Mountains could be an inspiration, to outline of California or coast line, a vineyard (of course), a vine...We are in silicon valley, so there is a map of silicon valley with the Bay and ocean, something from a map could work, or let your creativity flow and not use any of these concepts.
Should not have
• I do not not care for decorative fonts, however all else is open

```html
<!DOCTYPE html>
<html lang="en">
<head>
<meta charset="utf-8">
<title>Valmaren Wine Labels</title>
<link rel="stylesheet" href="https://fonts.googleapis.com/css2?family=Cinzel:wght@400;600;700&family=Marcellus&family=Libre+Caslon+Text&display=swap">
<style>
  :root {
    --paper: #f3f1ec;
    --paper-edge: #e6e2da;
    --frame: #4a2a24;
    --ink: #1d1b1a;
    --brand-gold: #8c7c45;
    --brand-shadow: #3c3522;
    --red-word: #d8262a;
    --olive-top: #1d2214;
    --olive-mid: #5f7530;
    --night-top: #1a1a16;
    --night-bottom: #12120f;
    --board-light: #ffffff;
    --scene-dark: #2e2e2c;
    --scene-light: #b9b8b2;
  }
  * { box-sizing: border-box; margin: 0; padding: 0; }
  html, body { width: 1200px; height: 2490px; overflow: hidden; background: var(--board-light); }
  .board { position: relative; width: 1200px; height: 2490px; }
  .panel { position: absolute; left: 0; width: 763px; }
  .panel--white-wine { top: 0; height: 1169px;
    background: linear-gradient(180deg, var(--olive-top) 0%, var(--olive-mid) 28%, var(--olive-mid) 36%, var(--olive-top) 70%, var(--night-top) 100%); }
  .panel--red-wine { top: 1169px; height: 1321px;
    background: linear-gradient(180deg, var(--night-top), var(--night-bottom)); }

  .label {
    position: absolute; width: 634px; height: 1063px;
    background: radial-gradient(circle at 40% 30%, var(--paper), var(--paper-edge));
    font-family: "Marcellus", serif; color: var(--ink); text-align: center;
  }
  .label__frame { position: absolute; inset: 14px; border: 5px solid var(--frame); }
  .label__brand {
    position: absolute; top: 95px; left: 0; right: 0;
    font-family: "Cinzel", serif; font-weight: 700; font-size: 74px; letter-spacing: 3px;
    color: var(--brand-gold); -webkit-text-stroke: 2px var(--brand-shadow); line-height: 1;
  }
  .label__phonetic {
    position: absolute; top: 182px; left: 0; right: 0;
    font-family: "Marcellus", serif; font-size: 50px; letter-spacing: 2px; color: var(--brand-gold);
    -webkit-text-stroke: 1px var(--brand-shadow); line-height: 1;
  }
  .label__scene {
    position: absolute; top: 250px; left: 14px; right: 14px; height: 390px;
    background: linear-gradient(180deg, var(--scene-light) 0%, #d6d5d0 25%, var(--scene-dark) 55%, #5e5d58 80%, var(--paper) 100%);
  }
  .label__variety {
    position: absolute; top: 695px; left: 0; right: 0;
    font-family: "Cinzel", serif; font-weight: 600; font-size: 100px; line-height: 1; letter-spacing: 2px;
  }
  .label__variety--white { color: var(--paper); -webkit-text-stroke: 3px var(--ink); }
  .label__variety--red { color: var(--red-word); }
  .label__wine {
    position: absolute; top: 800px; left: 0; right: 0;
    font-size: 66px; line-height: 1; letter-spacing: 2px;
  }
  .label__rule { position: absolute; top: 905px; left: 247px; width: 140px; height: 20px; }
  .label__facts {
    position: absolute; top: 965px; left: 50px; right: 50px;
    display: flex; justify-content: space-between;
    font-family: "Libre Caslon Text", serif; font-size: 34px; line-height: 1;
  }

  .label--large { left: 62px; }
  .panel--white-wine .label--large { top: 53px; }
  .panel--red-wine .label--large { top: 55px; }
  .label--small { left: 864px; transform: scale(0.35); transform-origin: top left; }
  .label--small.label--white { top: 432px; }
  .label--small.label--red { top: 1714px; }
</style>
</head>
<body>
<main class="board">
  <section class="panel panel--white-wine">
    <article class="label label--large label--white">
      <div class="label__frame"></div>
      <h1 class="label__brand">VALMAREN</h1>
      <p class="label__phonetic">[vahl-mah-ren]</p>
      <div class="label__scene" role="img" aria-label="Monochrome etching of terraced vineyard hills with a farmhouse, framed by grape clusters"></div>
      <p class="label__variety label__variety--white">WHITE</p>
      <p class="label__wine">WINE</p>
      <svg class="label__rule" viewBox="0 0 140 20"><line x1="0" y1="10" x2="140" y2="10" stroke="#4a2a24" stroke-width="2"/><rect x="63" y="3" width="14" height="14" transform="rotate(45 70 10)" fill="#4a2a24"/></svg>
      <p class="label__facts"><span>Net 750ml</span><span>12.5% alc./vol.</span></p>
    </article>
  </section>

  <section class="panel panel--red-wine">
    <article class="label label--large label--red">
      <div class="label__frame"></div>
      <h1 class="label__brand">VALMAREN</h1>
      <p class="label__phonetic">[vahl-mah-ren]</p>
      <div class="label__scene" role="img" aria-label="Monochrome etching of terraced vineyard hills with a farmhouse, framed by grape clusters"></div>
      <p class="label__variety label__variety--red">RED</p>
      <p class="label__wine">WINE</p>
      <svg class="label__rule" viewBox="0 0 140 20"><line x1="0" y1="10" x2="140" y2="10" stroke="#4a2a24" stroke-width="2"/><rect x="63" y="3" width="14" height="14" transform="rotate(45 70 10)" fill="#4a2a24"/></svg>
      <p class="label__facts"><span>Net 750ml</span><span>14.1% alc./vol.</span></p>
    </article>
  </section>

  <article class="label label--small label--white">
    <div class="label__frame"></div>
    <p class="label__brand">VALMAREN</p>
    <p class="label__phonetic">[vahl-mah-ren]</p>
    <div class="label__scene" role="img" aria-label="Monochrome etching of terraced vineyard hills with a farmhouse"></div>
    <p class="label__variety label__variety--white">WHITE</p>
    <p class="label__wine">WINE</p>
    <svg class="label__rule" viewBox="0 0 140 20"><line x1="0" y1="10" x2="140" y2="10" stroke="#4a2a24" stroke-width="2"/><rect x="63" y="3" width="14" height="14" transform="rotate(45 70 10)" fill="#4a2a24"/></svg>
    <p class="label__facts"><span>Net 750ml</span><span>12.5% alc./vol.</span></p>
  </article>

  <article class="label label--small label--red">
    <div class="label__frame"></div>
    <p class="label__brand">VALMAREN</p>
    <p class="label__phonetic">[vahl-mah-ren]</p>
    <div class="label__scene" role="img" aria-label="Monochrome etching of terraced vineyard hills with a farmhouse"></div>
    <p class="label__variety label__variety--red">RED</p>
    <p class="label__wine">WINE</p>
    <svg class="label__rule" viewBox="0 0 140 20"><line x1="0" y1="10" x2="140" y2="10" stroke="#4a2a24" stroke-width="2"/><rect x="63" y="3" width="14" height="14" transform="rotate(45 70 10)" fill="#4a2a24"/></svg>
    <p class="label__facts"><span>Net 750ml</span><span>14.1% alc./vol.</span></p>
  </article>
</main>
</body>
</html>
```